Rtvlegal.com needs a wedsite. Law Office of Bernard T. Whitfield

Bernard T. Whitfield is a criminal law firm that is 5 years old. We have already had all the content written and now just need the website designed. We also just finished our logo design using Pixel Harbor and would like it used in the design of the website.

Industry/Entity Type

Law Firm

Number of Pages Required

5+ page

Requirements
Must have
• I was our new logo to be on the website also. I want Dallas sites as the stock pictures for the website. For example the Grey Stone Hall. I also need to be able to add ClipNest videos. It has to adjust to be seen on computers and also cell phones. I need to be able to have a information sheet for clients to fill out and submit back to me.

```html
<!DOCTYPE html>
<html lang="en">
<head>
<meta charset="utf-8">
<title>Law Office of Bernard T. Whitfield</title>
<link href="https://fonts.googleapis.com/css2?family=Merriweather:wght@300;400;700&family=Roboto:wght@300;400&display=swap" rel="stylesheet">
<style>
  :root {
    --header-bg: #454545;
    --footer-bg: #3c3c3c;
    --page-bg: #f6f6f6;
    --navy: #0c3273;
    --slate: #4b4b4b;
    --coral: #d35656;
    --tab-grey: #c6c6c6;
    --rule: #e2e2e2;
    --rule-dark: #d0d0d0;
    --text: #8a8a8a;
    --heading: #555555;
    --white: #ffffff;
    --field: #505050;
  }
  * { box-sizing: border-box; margin: 0; padding: 0; }
  html, body { width: 722px; height: 1200px; overflow: hidden; background: var(--page-bg); }
  body { position: relative; font-family: "Merriweather", Georgia, serif; color: var(--text); }
  .abs { position: absolute; }

  .site-header { left: 0; top: 0; width: 722px; height: 68px; background: var(--header-bg); }
  .brand { display: flex; align-items: center; gap: 6px; }
  .site-header .brand { left: 168px; top: 14px; }
  .brand-dot { flex: none; width: 18px; height: 18px; border-radius: 50%; background: var(--navy); border: 2px solid var(--white); }
  .brand-name { color: var(--white); font-size: 7px; font-weight: 700; line-height: 9px; width: 62px; }
  .tagline { left: 260px; top: 14px; border-left: 1px solid #2e2e2e; padding-left: 14px; height: 26px; font-size: 7.8px; font-weight: 300; color: #8c8c8c; line-height: 13px; }
  .contact-box { left: 467px; top: 14px; width: 106px; height: 24px; background: #3a3a3a; border-radius: 2px; font-family: "Roboto", Arial, sans-serif; font-size: 7.2px; color: #cfcfcf; padding: 2px 6px; line-height: 10px; }
  .contact-box svg { vertical-align: -1px; margin-right: 4px; }

  .main-nav { left: 0; top: 68px; width: 722px; height: 39px; background: var(--white); }
  .main-nav ul { list-style: none; display: flex; position: absolute; left: 162px; top: 14px; gap: 15px; font-size: 7.8px; color: #777; }
  .main-nav li.active { color: var(--navy); position: relative; }
  .main-nav li.active::after { content: ""; position: absolute; left: -1px; right: -1px; top: 21px; height: 3px; background: #cfcfcf; }

  .hero { left: 0; top: 107px; width: 722px; height: 233px; background: linear-gradient(180deg, #4a7fc0 0%, #8fb0d6 35%, #b98a6a 65%, #a7642a 85%, #5a4a34 100%); }

  .arrows { display: flex; gap: 2px; }
  .arrow { width: 11px; height: 11px; background: #e1e1e1; border-radius: 1px; display: flex; align-items: center; justify-content: center; }
  .arrow.on { background: var(--coral); }

  .service-card { top: 366px; width: 135px; height: 100px; border-radius: 2px; color: var(--white); text-align: center; padding: 9px 8px 0; }
  .service-card h3 { font-size: 11px; font-weight: 700; line-height: 14px; height: 30px; }
  .service-card p { font-size: 7px; line-height: 10.5px; margin-top: 7px; height: 32px; }
  .service-card .more { font-size: 7.3px; margin-top: 7px; display: block; }
  .card-navy { left: 149px; background: var(--navy); }
  .card-slate { left: 293px; background: var(--slate); }
  .card-coral { left: 438px; background: var(--coral); }

  .section-title { font-size: 9px; color: #666; font-weight: 400; }
  .rule { height: 1px; background: var(--rule); }
  .rule::before { content: ""; display: block; width: 63px; height: 3px; margin-top: -1px; background: var(--rule-dark); }

  .team-photo { top: 533px; height: 82px; border-radius: 2px; }
  .tab { left: 149px; width: 135px; height: 27px; font-size: 9px; color: #555; background: var(--tab-grey); padding: 7px 9px; border-radius: 1px; }
  .tab.active { background: var(--navy); color: var(--white); }

  .profile-name { left: 306px; top: 636px; font-size: 16px; font-weight: 300; color: var(--heading); }
  .profile-bio { left: 306px; top: 665px; width: 268px; font-family: "Roboto", Arial, sans-serif; font-size: 6.9px; line-height: 10.4px; color: var(--text); }
  .btn { background: var(--navy); color: var(--white); font-size: 6.8px; text-align: center; border-radius: 2px; }

  .news-date { left: 149px; top: 891px; width: 30px; height: 32px; background: #5a5a5a; color: var(--white); text-align: center; border-radius: 1px; }
  .news-date b { display: block; font-size: 12px; font-weight: 400; line-height: 15px; margin-top: 2px; }
  .news-date span { display: block; font-size: 5.5px; color: #cfcfcf; line-height: 7px; }
  .news-title { left: 184px; top: 889px; width: 175px; font-size: 9.6px; line-height: 12px; color: var(--navy); }
  .news-meta { left: 184px; top: 916px; font-size: 5.8px; color: #777; }
  .news-excerpt { left: 149px; top: 932px; width: 212px; font-family: "Roboto", Arial, sans-serif; font-size: 6.8px; line-height: 10.4px; }
  .news-more { left: 149px; top: 968px; font-size: 7.5px; color: #777; }

  .video { left: 378px; top: 889px; width: 182px; height: 101px; background: #111; }
  .video-title { left: 2px; top: 1px; font-family: "Roboto", Arial, sans-serif; font-size: 5px; color: #ddd; }
  .video-frame { left: 55px; top: 10px; width: 72px; height: 74px; background: linear-gradient(180deg, #8c7a62, #5e4634 70%, #3a2a20); }
  .video-bar { left: 0; bottom: 9px; width: 182px; height: 2px; background: #555; }
  .video-bar i { display: block; width: 45px; height: 2px; background: #cc2020; }
  .video-controls { left: 0; bottom: 0; width: 182px; height: 9px; background: #1c1c1c; }

  .site-footer { left: 0; top: 1011px; width: 722px; height: 189px; background: var(--footer-bg); }
  .footer-brand { left: 152px; top: 1030px; }
  .footer-about { left: 152px; top: 1080px; width: 130px; font-family: "Roboto", Arial, sans-serif; font-size: 6.6px; line-height: 9.7px; color: #8f8f8f; }
  .footer-title { font-size: 8.6px; color: #d6d6d6; }
  .field { background: var(--field); font-family: "Roboto", Arial, sans-serif; font-size: 6.5px; color: #9b9b9b; padding: 4px 7px; border-radius: 1px; }
  .footer-note { font-family: "Roboto", Arial, sans-serif; font-size: 7px; color: #5e5e5e; }
  .footer-rule { left: 152px; top: 1171px; width: 421px; height: 1px; background: #6a6a6a; }
  .footer-rule::before { content: ""; display: block; width: 57px; height: 3px; margin-top: -2px; background: #d8d8d8; }
  .copyright { left: 152px; top: 1178px; font-size: 6.5px; color: #a8a8a8; }
</style>
</head>
<body>

<header class="site-header abs">
  <div class="brand abs">
    <span class="brand-dot"></span>
    <span class="brand-name">Law Office of Bernard T. Whitfield</span>
  </div>
  <p class="tagline abs">Our goal is to balance the scales<br>through zealous advocacy.</p>
  <div class="contact-box abs">
    <div><svg width="7" height="7" viewBox="0 0 10 10"><path d="M2 0.5l2 2.2-1 1.3c.7 1.4 1.6 2.3 3 3l1.3-1 2.2 2-1.3 1.7C4.5 9.5.5 5.5.3 1.8z" fill="#bbb"/></svg>214.555.0186</div>
    <div><svg width="7" height="7" viewBox="0 0 10 10"><circle cx="5" cy="5" r="4.5" fill="#bbb"/><path d="M.5 5h9M5 .5c-2.5 3-2.5 6 0 9M5 .5c2.5 3 2.5 6 0 9" stroke="#3a3a3a" stroke-width=".7" fill="none"/></svg>earlyreleasehelp.com</div>
  </div>
</header>

<nav class="main-nav abs">
  <ul>
    <li class="active">Attorney Profile</li>
    <li>How We Can Help</li>
    <li>Services <svg width="5" height="4" viewBox="0 0 5 4"><path d="M.5 1l2 2 2-2" stroke="#888" fill="none" stroke-width=".8"/></svg></li>
    <li>Contact Us</li>
  </ul>
</nav>

<div class="hero abs" role="img" aria-label="Dallas skyline with Grey Stone Hall and autumn trees under a blue sky"></div>

<div class="arrows abs" style="left:549px; top:351px;">
  <span class="arrow"><svg width="5" height="6" viewBox="0 0 5 6"><path d="M3.5 .8L1.3 3l2.2 2.2" stroke="#555" fill="none" stroke-width="1"/></svg></span>
  <span class="arrow on"><svg width="5" height="6" viewBox="0 0 5 6"><path d="M1.5 .8L3.7 3 1.5 5.2" stroke="#fff" fill="none" stroke-width="1"/></svg></span>
</div>

<article class="service-card card-navy abs">
  <h3>Murder and other homicide offenses</h3>
  <p>Our attorneys are knowledgeable about DNA, ballistic, fingerprint, fiber analysis...</p>
  <span class="more">Read More</span>
</article>
<article class="service-card card-slate abs">
  <h3>Expungements and non-disclosures</h3>
  <p>Our lawyers help you make a fresh start through criminal record expungement ...</p>
  <span class="more">Read More</span>
</article>
<article class="service-card card-coral abs">
  <h3>Early probation release</h3>
  <p>We help you put your mistakes behind you through early termination of your probation.</p>
  <span class="more">Read More</span>
</article>

<h2 class="section-title abs" style="left:149px; top:489px;">Our Team</h2>
<div class="rule abs" style="left:149px; top:512px; width:424px;"></div>

<div class="team-photo abs" style="left:149px; width:132px; background:linear-gradient(135deg,#5a3e2c,#8a6a4e 50%,#3a2a1e);" role="img" aria-label="Portrait of Bernard T. Whitfield in his office"></div>
<div class="team-photo abs" style="left:294px; width:132px; background:linear-gradient(135deg,#8a9a4a,#b8a070 50%,#6a7a3a);" role="img" aria-label="Portrait of Dana Morrow-Ellis outdoors"></div>
<div class="team-photo abs" style="left:441px; width:132px; background:linear-gradient(135deg,#d8d8d0,#5a4a38 55%,#3a2a1c);" role="img" aria-label="Portrait of Kyle Brandt in front of a bookshelf"></div>

<div class="tab active abs" style="top:641px;">Bernard T. Whitfield</div>
<div class="tab abs" style="top:672px;">Dana Morrow-Ellis</div>
<div class="tab abs" style="top:704px;">Kyle Brandt</div>

<h2 class="profile-name abs">Bernard T. Whitfield</h2>
<div class="profile-bio abs">
  <p>Bernard T. Whitfield is the managing partner of our law firm. Before founding his own practice, he worked for one of the best criminal defense law firms in the Dallas-Fort Worth area, where he advocated for clients accused of drug, murder, assault and other serious offenses.</p>
  <p>Bernard's lifelong career goal was to become a criminal defense trial attorney. His studies at Lakeview University School of Law reflect his single-minded intention of honing his courtroom skills and knowledge about criminal law. Bernard won several regional advocacy contests and was runner up in multiple national competitions. His professors and peers voted for Bernard as one of the ten best advocates in the school. He earned the Judge Harold P. Voss Scholarship and a position in the honor society National Guild of Trial Advocates.</p>
</div>
<div class="btn abs" style="left:306px; top:809px; width:40px; height:13px; line-height:13px;">Read more</div>

<h2 class="section-title abs" style="left:149px; top:847px;">News</h2>
<div class="rule abs" style="left:149px; top:869px; width:180px;"></div>
<div class="arrows abs" style="left:331px; top:865px;">
  <span class="arrow"><svg width="5" height="6" viewBox="0 0 5 6"><path d="M3.5 .8L1.3 3l2.2 2.2" stroke="#555" fill="none" stroke-width="1"/></svg></span>
  <span class="arrow"><svg width="5" height="6" viewBox="0 0 5 6"><path d="M1.5 .8L3.7 3 1.5 5.2" stroke="#555" fill="none" stroke-width="1"/></svg></span>
</div>

<h2 class="section-title abs" style="left:366px; top:847px;">Our Videos</h2>
<div class="rule abs" style="left:366px; top:869px; width:180px;"></div>
<div class="arrows abs" style="left:549px; top:865px;">
  <span class="arrow"><svg width="5" height="6" viewBox="0 0 5 6"><path d="M3.5 .8L1.3 3l2.2 2.2" stroke="#555" fill="none" stroke-width="1"/></svg></span>
  <span class="arrow"><svg width="5" height="6" viewBox="0 0 5 6"><path d="M1.5 .8L3.7 3 1.5 5.2" stroke="#555" fill="none" stroke-width="1"/></svg></span>
</div>

<div class="news-date abs"><b>27</b><span>March</span><span>2015</span></div>
<h3 class="news-title abs">Halvorsen LLP gets new CEO in Martin Reyes.</h3>
<p class="news-meta abs">Paul Lindqvist / 0 Comments</p>
<p class="news-excerpt abs">Halvorsen LLP, a Dallas-based law firm with a large presence in Austin and Houston, has a new CEO and board chairman in Martin Reyes.</p>
<p class="news-more abs">Read more</p>

<div class="video abs">
  <span class="video-title abs">Difference Between Expungement and Non...</span>
  <div class="video-frame abs" role="img" aria-label="Video still of the attorney standing in his office"></div>
  <svg class="abs" style="left:84px; top:40px;" width="14" height="14" viewBox="0 0 14 14"><path d="M3 1.5v11l9.5-5.5z" fill="#f2f2f2"/></svg>
  <div class="video-bar abs"><i></i></div>
  <div class="video-controls abs"></div>
</div>

<footer class="site-footer abs"></footer>
<div class="brand footer-brand abs">
  <span class="brand-dot"></span>
  <span class="brand-name">Law Office of Bernard T. Whitfield</span>
</div>
<p class="footer-about abs">The Law Office of Bernard T. Whitfield was founded on the principle embedded in the U.S. Constitution, which states not only that all men are created equal, but that everyone is innocent until proven guilty.</p>

<h3 class="footer-title abs" style="left:296px; top:1030px;">Quick Contact</h3>
<div class="field abs" style="left:295px; top:1059px; width:132px; height:15px;">Name...</div>
<div class="field abs" style="left:295px; top:1079px; width:132px; height:16px;">Email...</div>
<div class="field abs" style="left:295px; top:1100px; width:132px; height:34px;">Message...</div>
<div class="btn abs" style="left:388px; top:1141px; width:39px; height:12px; line-height:12px;">Submit</div>

<h3 class="footer-title abs" style="left:442px; top:1030px;">Newsletter</h3>
<p class="footer-note abs" style="left:442px; top:1057px;">Subscribe to our newsletter</p>
<div class="field abs" style="left:440px; top:1072px; width:133px; height:16px;">Email...</div>
<div class="btn abs" style="left:533px; top:1094px; width:39px; height:12px; line-height:12px;">Subscribe</div>

<div class="footer-rule abs"></div>
<p class="copyright abs">© Copyright information here</p>

</body>
</html>
```